Home inspection business! professional look attracting customers just by looks. Read must haves

its a new business I started on my own for home inspections I would like something very professional to give to real estate agents and clients, its going to have my license number on it my business phone number my name my website as well etc on the back side it will be servicing areas and also what kind of services I offer I also have a business card from someone else the way I would like mine to be. I will attach my logo

Home Inspection

listed in nice to haves

• phone number - 555 293 8471
• website- hollowpinecheck.com
• license number #2938475610
• my name Gavin keropulis
• picture of my logo and me on the front
• on the back of the card. stating I am servicing All of New York and Long Island
• also services I will offer will be home inspection -mold inspection -lead inspection -radon inspection -Termite Inspection -Infared Scan.
• and also we provide inspections for single family homes condos co-ops town-homes
• and commercial property
• same colors as the logos and also if you recommend fonts to look like the logo not sure up to you

```html
<!DOCTYPE html>
<html lang="en">
<head>
<meta charset="utf-8">
<title>Hollow Pine Check Home Inspectors – Business Card</title>
<link rel="stylesheet" href="https://fonts.googleapis.com/css2?family=Montserrat:wght@400;500;600&display=swap">
<style>
  :root {
    --brand-blue: #009fe3;
    --brand-gray: #9b9b9b;
    --ink: #4a4a4a;
    --faint: #e9e9e9;
    --paper: #ffffff;
    --backdrop: #b4b4b4;
  }
  * { box-sizing: border-box; margin: 0; padding: 0; }
  html, body { width: 1200px; height: 1200px; overflow: hidden; }
  body {
    background: var(--backdrop);
    font-family: "Montserrat", sans-serif;
    color: var(--ink);
    position: relative;
  }
  .card {
    position: absolute;
    left: 244px;
    width: 711px;
    height: 408px;
    background: var(--paper);
    overflow: hidden;
  }
  .card--front { top: 173px; }
  .card--back { top: 645px; }

  .rule-gray {
    position: absolute; left: 0; right: 0; top: 349px; height: 11px;
    background: var(--brand-gray);
  }
  .band-blue {
    position: absolute; left: 0; right: 0; top: 368px; height: 40px;
    background: var(--brand-blue);
  }

  .brand {
    display: flex; align-items: center; gap: 10px;
    color: var(--brand-blue);
    font-weight: 600;
    text-transform: uppercase;
    line-height: 1.15;
  }
  .brand__dot {
    flex: none; border-radius: 50%;
    background: var(--brand-blue);
  }

  /* Front */
  .card--front .brand {
    position: absolute; left: 46px; top: 62px;
    font-size: 22px; width: 300px;
  }
  .card--front .brand__dot { width: 44px; height: 44px; }
  .holder-name {
    position: absolute; left: 45px; top: 166px;
    font-size: 30px; font-weight: 500; color: var(--brand-blue);
    letter-spacing: 0.2px;
  }
  .holder-title {
    position: absolute; left: 46px; top: 206px;
    font-size: 13.5px; font-weight: 400; color: var(--ink);
  }
  .contact-list {
    position: absolute; left: 46px; top: 248px;
    list-style: none;
  }
  .contact-list li {
    display: flex; align-items: center; gap: 8px;
    height: 23.5px;
    font-size: 14.5px; font-weight: 500; color: var(--ink);
  }
  .contact-list svg { width: 15px; height: 15px; flex: none; fill: var(--brand-blue); }
  .side-mark {
    position: absolute; right: 82px; top: 40px;
    writing-mode: vertical-rl;
    font-size: 24px; font-weight: 600; text-transform: uppercase;
    color: var(--faint); letter-spacing: 0.5px;
  }

  /* Back */
  .card--back .brand {
    position: absolute; left: 0; right: 0; top: 72px;
    justify-content: center;
    font-size: 24px;
  }
  .card--back .brand__dot { width: 40px; height: 40px; }
  .coverage {
    position: absolute; left: 0; right: 0; top: 200px;
    text-align: center;
    font-size: 18px; font-weight: 400; line-height: 25px; color: var(--ink);
  }
  .property-types {
    position: absolute; left: 0; right: 0; top: 287px;
    text-align: center;
    font-size: 15.5px; font-weight: 400; line-height: 22px; color: var(--brand-blue);
  }
  .license {
    position: absolute; right: 15px; top: 368px; height: 40px;
    display: flex; align-items: center;
    font-size: 19px; font-weight: 600; color: #fff; letter-spacing: 0.3px;
    word-spacing: 3px;
  }
</style>
</head>
<body>

<section class="card card--front">
  <div class="brand">
    <span class="brand__dot"></span>
    <span>Hollow Pine Check<br>Home Inspectors</span>
  </div>
  <div class="side-mark">Hollow Pine Check</div>

  <h1 class="holder-name">Gavin Keropulis</h1>
  <p class="holder-title">Certified Home Inspector</p>

  <ul class="contact-list">
    <li>
      <svg viewBox="0 0 24 24" aria-hidden="true"><path d="M6.6 10.8a15.1 15.1 0 0 0 6.6 6.6l2.2-2.2c.3-.3.7-.4 1-.2 1.1.4 2.3.6 3.6.6.6 0 1 .4 1 1V20c0 .6-.4 1-1 1C10.6 21 3 13.4 3 4c0-.6.4-1 1-1h3.5c.6 0 1 .4 1 1 0 1.3.2 2.5.6 3.6.1.3 0 .7-.2 1L6.6 10.8z"/></svg>
      555 293 8471
    </li>
    <li>
      <svg viewBox="0 0 24 24" aria-hidden="true"><path d="M12 2a10 10 0 1 0 0 20 10 10 0 0 0 0-20zm6.9 6h-2.9a15.7 15.7 0 0 0-1.4-3.6A8 8 0 0 1 18.9 8zM12 4c.8 1.2 1.5 2.5 1.9 4h-3.8c.4-1.4 1.1-2.8 1.9-4zM4.3 14a8.2 8.2 0 0 1 0-4h3.4a16.5 16.5 0 0 0 0 4H4.3zm.8 2h2.9c.3 1.3.8 2.5 1.4 3.6A8 8 0 0 1 5.1 16zM8 8H5.1a8 8 0 0 1 4.3-3.6C8.8 5.5 8.3 6.7 8 8zm4 12c-.8-1.2-1.5-2.5-1.9-4h3.8c-.4 1.4-1.1 2.8-1.9 4zm2.3-6H9.7a14.700 14.7 0 0 1 0-4h4.6a14.7 14.7 0 0 1 0 4zm.3 5.6c.6-1.1 1.1-2.3 1.4-3.6h2.9a8 8 0 0 1-4.3 3.6zm1.7-5.6a16.5 16.5 0 0 0 0-4h3.4a8.2 8.2 0 0 1 0 4h-3.4z"/></svg>
      hollowpinecheck.com
    </li>
    <li>
      <svg viewBox="0 0 24 24" aria-hidden="true"><path d="M2 5h20v14H2V5zm2 2v.5l8 5.5 8-5.5V7H4zm0 3v7h16v-7l-8 5.5L4 10z"/></svg>
      gavin@hollowpinecheck.com
    </li>
    <li>
      <svg viewBox="0 0 24 24" aria-hidden="true"><path d="M12 2a7 7 0 0 0-7 7c0 5.2 7 13 7 13s7-7.8 7-13a7 7 0 0 0-7-7zm0 9.5A2.5 2.5 0 1 1 12 6.5a2.5 2.5 0 0 1 0 5z"/></svg>
      48-17 Crescent Ave, Oakmere, NY 11502
    </li>
  </ul>

  <div class="rule-gray"></div>
  <div class="band-blue"></div>
</section>

<section class="card card--back">
  <div class="brand">
    <span class="brand__dot"></span>
    <span>Hollow Pine Check<br>Home Inspectors</span>
  </div>

  <p class="coverage">
    We servicing All of New York and Long Island<br>
    also We Offer home inspection,mold ispection,<br>
    lead inspection,radon inspection,Termite Inspection,infrared Scan
  </p>
  <p class="property-types">
    Also We Provide inspection for single Family<br>
    homes And Commercial property
  </p>

  <div class="rule-gray"></div>
  <div class="band-blue"></div>
  <p class="license">License number #2938475610</p>
</section>

</body>
</html>
```